K R Guard Systems - Alarm and CCTV installation Flyer

Need a flyer designed that grabs the attention of potential customers, we need the price to stand out the most to grab people’s attention, whether they are residential or commercial.We are a security company based in Brentwood Essex but cover London and the home counties. here is our website to take a look at www.krguardsystems.co.uk. We want them to know we install complete alarm and Cctv systems and will keep them “safe”

Target Market(s)

residential and commercial property

Colors
f37122

Requirements
Must have
• on one side
• large clear logo - professional design
• - Intruder Alarms starting from £495 + VAT. (Big text)
• - £150 discount on installations
• *terms and conditions apply (small text)
• - Not happy with your current provider? Free of charge no obligation take over survey and quotation and up to £100 off
• - CCTV systems starting from £595 + VAT (based on 2 cameras)
• K R Guard Systems are always there, always available, wherever and whenever you need us.
• Large telephone number at the bottom 01632 960418
• Address / email / website as a footer * see website for details
• on second side
• large and bold
• Are you looking to keep you and your premises safe?
• - K R Guard Systems install, maintain and repair all intruder alarms, CCTV, intercom and access control
• - View, control and manage your security systems anywhere in the world
• - Feel at ease with monitoring services & police response tailored to suit you and your business
• - K R Guard can takeover any existing security system and offer maintenance checks to guarantee the best performance for you and your premises
• - K R Guard understand that being security conscious is ever increasing, protecting your property and family is a number one priority
• - Our fully insured and accredited team offer quality, safety and cost efficiency throughout the whole process
• - K R Guard Systems are using the latest cloud-based technology to stay connected with your home and business 24/7
• If you are looking to improve the security in your home, office or commercial property then call a member of our team today for a free quote.
• Fully insured and accredited
• Tradeproof logo and NWBQC Intruder and CCTV logos
• Logo somewhere on page and
• Telephone number
• Address / email / website as footer
Nice to have
• We would like to have the text saying
• Intruder alarms installed from £495 + vat the biggest text on the page. Most likely the £495 part the largest.
• Also would like “not happy with your current provider” more obvious
• We would like use our company colours - Orange/White/black

```html
<!DOCTYPE html>
<html lang="en">
<head>
<meta charset="utf-8">
<title>K R Guard Systems – Flyer</title>
<link rel="stylesheet" href="https://fonts.googleapis.com/css2?family=Roboto+Condensed:wght@300;400;700&display=swap">
<style>
:root{
  --red:#e52421;
  --red-deep:#b01818;
  --black:#0d0d0d;
  --white:#ffffff;
  --stage:#a6a6a6;
  --photo-red-a:#c8201c;
  --photo-red-b:#7a0f0d;
  --photo-grey-a:#e6e4e1;
  --photo-grey-b:#b9b6b1;
  --font:"Roboto Condensed", "Arial Narrow", sans-serif;
}
*{box-sizing:border-box;margin:0;padding:0}
html,body{width:1200px;height:841px;overflow:hidden}
body{background:var(--stage);font-family:var(--font);position:relative}
.flyer{position:absolute;top:62px;width:500px;height:700px;background:var(--black);overflow:hidden;color:var(--white)}
.flyer--info{left:88px}
.flyer--offer{left:614px}

/* ---------- shared footer ---------- */
.footer{position:absolute;left:0;right:0;bottom:0;height:102px;background:var(--red);text-align:center}
.footer__line{font-size:13px;font-weight:400;display:flex;justify-content:center;align-items:center;gap:6px;margin-top:6px;line-height:16px}
.footer__line:first-child{margin-top:8px}
.footer__line svg{width:10px;height:10px;fill:var(--white)}
.footer__phone{font-size:42px;font-weight:700;display:flex;justify-content:center;align-items:center;gap:14px;margin-top:2px;letter-spacing:.5px}
.footer__phone svg{width:26px;height:32px;fill:var(--white)}

/* ---------- brand block ---------- */
.brand{position:absolute;display:flex;flex-direction:column;align-items:center;justify-content:center;text-align:center}
.brand svg.hex{position:absolute;inset:0;width:100%;height:100%}
.brand__name{position:relative;color:var(--red);font-weight:400;line-height:1.05;letter-spacing:.5px}
.brand__mark{position:relative;width:26px;height:26px;background:var(--red);margin-bottom:8px}

/* ---------- info side ---------- */
.hero-photo{position:absolute;left:0;top:0;width:500px;height:273px;background:linear-gradient(120deg,var(--photo-red-a),var(--photo-red-b))}
.headline{position:absolute;left:32px;top:22px;text-transform:uppercase}
.headline span{display:block;white-space:nowrap}
.headline .light{font-weight:300;color:var(--white);font-size:46px;line-height:44px}
.headline .bold{font-weight:700;color:var(--black);font-size:58px;line-height:54px}
.intro{position:absolute;left:32px;top:279px;width:440px;font-size:11.4px;line-height:13.2px;font-weight:400}
.intro b,.cloud b{color:var(--red);font-weight:700}
.cloud{position:absolute;left:32px;top:393px;width:432px;height:80px;background:var(--white);display:flex}
.cloud__photo{flex:none;width:250px;height:80px;background:linear-gradient(90deg,#c9d6de,#eeeae3)}
.cloud__text{color:var(--black);font-size:13.5px;line-height:15.6px;padding:3px 6px 0 7px}
.accredited{position:absolute;left:32px;top:494px;width:155px;height:46px;border:1.5px solid var(--red);color:var(--red);font-weight:700;font-size:16px;line-height:19px;text-align:center;padding-top:3px;text-transform:uppercase}
.terms{position:absolute;left:38px;top:545px;font-size:8px;color:#ddd}
.badges{position:absolute;left:197px;top:485px;width:267px;height:64px;background:var(--white);display:flex;align-items:center;justify-content:space-around;padding:0 8px}
.badge-bar{width:110px;height:30px;background:#d9d9d9}
.badge-dot{width:38px;height:38px;border-radius:50%;background:#cfcfcf}
.badge-sq{width:34px;height:38px;background:#cfcfcf}
.cta{position:absolute;left:0;right:0;top:564px;text-align:center;font-size:12px}
.cta strong{display:block;color:var(--red);font-size:14.5px;font-weight:700;margin-top:2px}

/* ---------- offer side ---------- */
.keypad-photo{position:absolute;inset:0;background:linear-gradient(135deg,var(--photo-grey-a),var(--photo-grey-b))}
.offer-dark{position:absolute;left:0;top:0;width:500px;height:700px}
.offer-dark polygon{fill:var(--black)}
.offer-lede{position:absolute;left:186px;top:242px;font-size:19px;line-height:22px;font-weight:700;text-transform:uppercase}
.price{position:absolute;left:184px;top:246px;width:290px;height:150px}
.price__pound{position:absolute;left:0;top:14px;font-size:46px;line-height:1;font-weight:300}
.price__num{position:absolute;left:22px;top:0;font-size:168px;font-weight:300;color:var(--red);letter-spacing:-4px;line-height:1}
.price__vat{position:absolute;left:198px;top:84px;font-size:24px;line-height:1;font-weight:400}
.discount{position:absolute;right:30px;top:390px;font-size:15.5px;line-height:18px;font-weight:700}
.provider{position:absolute;left:34px;top:418px;text-transform:uppercase}
.provider .light{display:block;color:var(--red);font-size:34px;line-height:32px;font-weight:300;white-space:nowrap}
.provider .bold{display:block;color:var(--white);font-size:50px;line-height:46px;font-weight:700;white-space:nowrap}
.provider-note{position:absolute;left:34px;top:497px;font-size:11.6px;line-height:14px;white-space:nowrap}
.cctv{position:absolute;left:187px;top:516px;width:283px;height:54px;border:1.5px solid var(--red);display:flex;align-items:center;padding-left:10px}
.cctv__label{font-weight:700;font-size:16.5px;line-height:20px;text-transform:uppercase}
.cctv__price{position:absolute;left:146px;top:-3px;color:var(--red);font-size:46px;line-height:46px;font-weight:300}
.cctv__vat{position:absolute;left:254px;top:4px;font-size:12px;line-height:14px;writing-mode:vertical-rl}
.cctv__note{position:absolute;left:150px;top:40px;font-size:8.5px;line-height:10px}
.promise{position:absolute;left:36px;top:578px;width:436px;height:17px;background:var(--white);transform:skewX(-14deg);display:flex;align-items:center;justify-content:center}
.promise span{color:var(--red);font-size:10.5px;font-weight:700;transform:skewX(14deg)}
</style>
</head>
<body>

<section class="flyer flyer--info">
  <div class="hero-photo" role="img" aria-label="Red-toned photo of a home alarm keypad by a staircase"></div>
  <h1 class="headline">
    <span class="light">Are you</span>
    <span class="bold">Looking</span>
    <span class="light">to keep</span>
    <span class="light">you and your</span>
    <span class="bold">Premises safe?</span>
  </h1>

  <div class="brand" style="left:333px;top:30px;width:122px;height:142px">
    <svg class="hex" viewBox="0 0 122 142" aria-hidden="true"><polygon points="61,0 122,35 122,107 61,142 0,107 0,35" fill="#fff"/></svg>
    <span class="brand__mark"></span>
    <span class="brand__name" style="font-size:17px">K R GUARD<br>SYSTEMS</span>
  </div>

  <p class="intro"><b>K R Guard Systems</b> install, maintain and repair all intruder alarms, CCTV, intercom and access control view, control and manage your security systems anywhere in the world feel at ease with monitoring services &amp; police response tailored to suit you and your business. <b>K R Guard</b> can takeover any existing security system and offer maintenance checks to guarantee the best performance for you and your premises. <b>K R Guard</b> understand that being security conscious is ever increasing, protecting your property and family is a number one priority. Our fully insured and accredited team offer quality, safety and cost efficiency throughout the whole process</p>

  <div class="cloud">
    <div class="cloud__photo" role="img" aria-label="Smartphones showing a security app beside a modern kitchen"></div>
    <p class="cloud__text"><b>K R Guard Systems</b> are using the latest cloud-based technology to stay connected with your home and business <b>24/7</b></p>
  </div>

  <div class="accredited">Fully insured<br>and accredited</div>
  <p class="terms">*Terms and conditions apply</p>
  <div class="badges" role="img" aria-label="Tradeproof membership and NWBQC intruder and CCTV accreditation badges">
    <span class="badge-bar"></span><span class="badge-dot"></span><span class="badge-sq"></span><span class="badge-dot"></span>
  </div>

  <p class="cta">If you are looking to improve the security in your home, office or commercial property then
    <strong>call a member of our team today for a free quote.</strong></p>

  <footer class="footer">
    <p class="footer__line"><svg viewBox="0 0 10 10"><path d="M5 0a3.5 3.5 0 0 0-3.5 3.5C1.5 6 5 10 5 10s3.5-4 3.5-6.5A3.5 3.5 0 0 0 5 0zm0 5a1.5 1.5 0 1 1 0-3 1.5 1.5 0 0 1 0 3z"/></svg>14 Harlow Lane, Brentwood, Essex, CM14 9ZX</p>
    <p class="footer__line"><svg viewBox="0 0 10 10"><rect x="0" y="2" width="10" height="7"/></svg>operations@krguardsystems.co.uk&nbsp;&nbsp;&nbsp;&nbsp;<svg viewBox="0 0 10 10"><circle cx="5" cy="5" r="5"/></svg>www.krguardsystems.co.uk</p>
    <p class="footer__phone"><svg viewBox="0 0 24 30"><path d="M6 1l5 7-3 3c1 4 4 8 7 10l3-3 6 5-3 5C11 27 2 16 1 5z"/></svg>01632 960418</p>
  </footer>
</section>

<section class="flyer flyer--offer">
  <div class="keypad-photo" role="img" aria-label="Hand pressing a wall-mounted alarm keypad reading Welcome Home, behind a hexagon pattern"></div>
  <svg class="offer-dark" viewBox="0 0 500 700" aria-hidden="true">
    <polygon points="0,405 80,370 170,370 170,248 260,216 500,216 500,700 0,700"/>
  </svg>

  <div class="brand" style="left:264px;top:20px;width:186px;height:200px">
    <svg class="hex" viewBox="0 0 186 200" aria-hidden="true"><polygon points="93,2 184,52 184,148 93,198 2,148 2,52" fill="#fff" stroke="#e52421" stroke-width="3"/></svg>
    <span class="brand__mark"></span>
    <span class="brand__name" style="font-size:24px">K R GUARD<br>SYSTEMS</span>
  </div>

  <p class="offer-lede">Intruder alarms starting from</p>
  <div class="price">
    <span class="price__pound">£</span>
    <span class="price__num">495</span>
    <span class="price__vat">+VAT</span>
  </div>
  <p class="discount">£150 discount on installations</p>

  <h2 class="provider"><span class="light">Not happy with your</span><span class="bold">Current provider?</span></h2>
  <p class="provider-note">Free of charge no obligation take over survey and quotation and up to £100 off</p>

  <div class="cctv">
    <span class="cctv__label">CCTV systems<br>starting from</span>
    <span class="cctv__price">£595</span>
    <span class="cctv__vat">+VAT</span>
    <span class="cctv__note">(based on 2 cameras)</span>
  </div>

  <div class="promise"><span>K R Guard Systems are always there, always available, wherever and whenever you need us.</span></div>

  <footer class="footer">
    <p class="footer__line"><svg viewBox="0 0 10 10"><path d="M5 0a3.5 3.5 0 0 0-3.5 3.5C1.5 6 5 10 5 10s3.5-4 3.5-6.5A3.5 3.5 0 0 0 5 0zm0 5a1.5 1.5 0 1 1 0-3 1.5 1.5 0 0 1 0 3z"/></svg>14 Harlow Lane, Brentwood, Essex, CM14 9ZX</p>
    <p class="footer__line"><svg viewBox="0 0 10 10"><rect x="0" y="2" width="10" height="7"/></svg>operations@krguardsystems.co.uk&nbsp;&nbsp;&nbsp;&nbsp;<svg viewBox="0 0 10 10"><circle cx="5" cy="5" r="5"/></svg>www.krguardsystems.co.uk</p>
    <p class="footer__phone"><svg viewBox="0 0 24 30"><path d="M6 1l5 7-3 3c1 4 4 8 7 10l3-3 6 5-3 5C11 27 2 16 1 5z"/></svg>01632 960418</p>
  </footer>
</section>

</body>
</html>
```